Tenbrook Business Card Design

We are the largest used car company fro JapanJust need a simple business cards to start with

Industry/Entity Type

Used Car

Contact Information for Business Card

Haruna " Ned" Morikawa
Operations Director
Tenbrook Australia Pty.Ltd.
P.O.Box 517 Pendlestone NSW 2093
M: 0466 518 274
P: 1800 574 392
email : haruna.morikawa@tnbk.co.jp

```html
<!DOCTYPE html>
<html lang="en">
<head>
<meta charset="utf-8">
<title>Tenbrook Business Card Design</title>
<link rel="stylesheet" href="https://fonts.googleapis.com/css2?family=Source+Sans+3:wght@400;600;700&display=swap">
<style>
  :root {
    --backdrop: #d9d9d9;
    --card: #f6f6f4;
    --ink: #141414;
    --ink-soft: #5a5a5a;
    --accent: #b3161c;
    --rule-dark: #111111;
  }
  * { box-sizing: border-box; margin: 0; padding: 0; }
  html, body {
    width: 1200px;
    height: 1200px;
    overflow: hidden;
    background: var(--backdrop);
    font-family: "Source Sans 3", sans-serif;
  }
  .business-card {
    position: absolute;
    left: 100px;
    top: 300px;
    width: 1000px;
    height: 600px;
    background: var(--card);
    box-shadow: 0 6px 18px rgba(0,0,0,0.18);
  }
  .brand {
    position: absolute;
    right: 70px;
    top: 92px;
    text-align: right;
  }
  .brand-name {
    font-size: 96px;
    font-weight: 700;
    line-height: 1;
    color: var(--ink);
    letter-spacing: 0.5px;
  }
  .brand-entity {
    font-size: 42px;
    font-weight: 600;
    line-height: 1.05;
    color: var(--ink-soft);
    letter-spacing: 0.5px;
  }
  .divider-rule {
    position: absolute;
    left: 430px;
    right: 25px;
    top: 272px;
    height: 7px;
    background: linear-gradient(to right, rgba(17,17,17,0) 0%, rgba(17,17,17,0.35) 40%, var(--rule-dark) 100%);
  }
  .contact-person {
    position: absolute;
    left: 62px;
    top: 198px;
  }
  .person-name {
    font-size: 33px;
    font-weight: 700;
    color: var(--ink);
    line-height: 1.1;
  }
  .person-role {
    font-size: 25px;
    font-weight: 400;
    color: var(--ink-soft);
    line-height: 1.2;
  }
  .contact-list {
    list-style: none;
    margin-top: 18px;
  }
  .contact-item {
    display: flex;
    align-items: flex-start;
    font-size: 28px;
    line-height: 1.15;
    color: var(--ink);
  }
  .contact-icon {
    width: 20px;
    height: 20px;
    margin: 5px 14px 0 0;
    flex: none;
    fill: var(--accent);
  }
</style>
</head>
<body>
  <section class="business-card">
    <div class="brand">
      <div class="brand-name">Tenbrook</div>
      <div class="brand-entity">Australia Pty.Ltd</div>
    </div>
    <div class="divider-rule"></div>
    <div class="contact-person">
      <div class="person-name">Haruna "Ned" Morikawa</div>
      <div class="person-role">Operations Director</div>
      <ul class="contact-list">
        <li class="contact-item">
          <svg class="contact-icon" viewBox="0 0 20 20" aria-hidden="true">
            <rect x="5" y="1" width="10" height="18" rx="2"/>
            <rect x="7" y="4" width="6" height="9" fill="#ffffff"/>
          </svg>
          0466 - 518 - 274
        </li>
        <li class="contact-item">
          <svg class="contact-icon" viewBox="0 0 20 20" aria-hidden="true">
            <path d="M5 2 L8 2 L9 6 L7 8 C8 11 9 12 12 13 L14 11 L18 12 L18 15 C18 17 16 18 14 18 C7 17 3 13 2 6 C2 4 3 2 5 2 Z"/>
          </svg>
          1800 - 574 - 392
        </li>
        <li class="contact-item">
          <svg class="contact-icon" viewBox="0 0 20 20" aria-hidden="true">
            <path d="M10 1 L19 9 L16 9 L16 18 L12 18 L12 13 L8 13 L8 18 L4 18 L4 9 L1 9 Z"/>
          </svg>
          <span>P.O.Box 517 Pendlestone<br>NSW 2093</span>
        </li>
      </ul>
    </div>
  </section>
</body>
</html>
```